Medical software helping patients with dry eye disease needs a business card

We have a logo we just need a design for a business card for a Canadian company called LUMA Ocular. We use AI technology to assist optometrists in properly diagnosing patients with dry eye disease reducing wait times in doctors offices and accuracy of diagnosis as well as identifying key possible indicators and tailored treatment plans. The final design should be clean and medical looking. Our mission is to help patients and our logo using blues and whites.

```html
<!DOCTYPE html>
<html lang="en">
<head>
<meta charset="utf-8">
<title>LUMA Ocular – Business Card</title>
<link href="https://fonts.googleapis.com/css2?family=Arimo:wght@400;700&display=swap" rel="stylesheet">
<style>
  :root {
    --navy: #0f4478;
    --navy-raised: #1d5791;
    --sky: #2aa7e3;
    --white: #ffffff;
    --paper: #e8e8ea;
    --faint: rgba(255, 255, 255, 0.08);
  }
  * { margin: 0; padding: 0; box-sizing: border-box; }
  html, body {
    width: 1200px; height: 802px; overflow: hidden;
    background: var(--paper);
    font-family: "Arimo", Arial, sans-serif;
  }
  .stage {
    position: relative; width: 1200px; height: 802px;
    display: flex; align-items: center; justify-content: center; gap: 40px;
  }
  .card {
    position: relative; width: 525px; height: 300px;
    background: var(--navy); overflow: hidden;
  }

  /* Front */
  .card-front .decor-circle {
    position: absolute; right: 30px; top: 70px;
    width: 190px; height: 190px; border-radius: 50%;
    background: var(--faint);
  }
  .card-front .corner-tab {
    position: absolute; right: 0; top: 0;
    width: 26px; height: 10px; background: var(--sky);
  }
  .card-front .edge-band {
    position: absolute; left: 0; right: 0; bottom: 0; height: 10px; display: flex;
  }
  .edge-band .band-white { flex: 0 0 55%; background: var(--white); }
  .edge-band .band-sky { flex: 1; background: var(--sky); }

  .brand {
    position: absolute; left: 32px; top: 112px;
    display: flex; align-items: center; gap: 12px;
  }
  .brand-dot { width: 34px; height: 34px; border-radius: 50%; background: var(--sky); }
  .brand-name { color: var(--white); font-weight: 700; font-size: 32px; letter-spacing: 0.5px; }

  .person { position: absolute; right: 32px; top: 34px; text-align: right; }
  .person-name {
    color: var(--sky); font-size: 21px; letter-spacing: 1px; text-transform: uppercase;
  }
  .person-role { color: var(--white); font-size: 14px; margin-top: 2px; }

  .contact {
    position: absolute; left: 32px; bottom: 36px;
    list-style: none; color: var(--white); font-size: 13px; line-height: 19px;
  }
  .contact li { display: flex; align-items: center; gap: 8px; }
  .contact svg { width: 11px; height: 11px; flex: none; }
  .contact .address { margin-top: 6px; display: block; line-height: 18px; }

  /* Back */
  .card-back { display: flex; align-items: center; justify-content: center; gap: 14px; }
  .card-back .brand-dot { background: var(--navy-raised); width: 44px; height: 44px; }
  .card-back .brand-name { color: var(--navy-raised); font-size: 44px; }
</style>
</head>
<body>
<main class="stage">
  <section class="card card-front">
    <div class="decor-circle" role="img" aria-label="Faint oversized brand mark decoration"></div>
    <div class="corner-tab"></div>

    <div class="brand">
      <span class="brand-dot"></span>
      <span class="brand-name">LUMA Ocular</span>
    </div>

    <div class="person">
      <p class="person-name">Daniel Harper</p>
      <p class="person-role">Manager</p>
    </div>

    <ul class="contact">
      <li>
        <svg viewBox="0 0 12 12"><path fill="#2aa7e3" d="M2.5 1l2 2.2-1 1.3a7 7 0 0 0 4 4l1.3-1 2.2 2-1.2 1.5C5.5 11 1 6.5 1 2.2z"/></svg>
        555-014-3872
      </li>
      <li>
        <svg viewBox="0 0 12 12"><rect x="1" y="2.5" width="10" height="7" fill="#2aa7e3"/><path d="M1 2.5l5 4 5-4" stroke="#0f4478" stroke-width="1" fill="none"/></svg>
        info@lumaocular.com
      </li>
      <li>
        <svg viewBox="0 0 12 12"><circle cx="6" cy="6" r="5" fill="#2aa7e3"/><path d="M1 6h10M6 1c2.5 3 2.5 7 0 10M6 1c-2.5 3-2.5 7 0 10" stroke="#0f4478" stroke-width="0.9" fill="none"/></svg>
        www.lumaocular.com
      </li>
      <li class="address">#210 845 Marlow St SW<br>Calgary, AB T2P 3K8</li>
    </ul>

    <div class="edge-band"><span class="band-white"></span><span class="band-sky"></span></div>
  </section>

  <section class="card card-back">
    <span class="brand-dot"></span>
    <span class="brand-name">LUMA Ocular</span>
  </section>
</main>
</body>
</html>
```